Modern Business Card Design Needed for Young Realtor

Information that is going on the card:Marvin Pold
Broker/Owner
555.210.3367
Marvin@MPoldRealty.com
www.MPoldRealty.com

Would also like to include my Instagram Handle somewhere. Probably on the back: the_queencity_realtorMy previous business card is attached, I like that one but would like an updated version and maybe a few design changes

Marvin Pold
Broker/Owner
555.210.3367
Marvin@MPoldRealty.com
www.MPoldRealty.com

• Would also like to include my Instagram Handle somewhere. Probably on the back: the_pinecrest_realtor
• Dorrance Hale or the DH (logo from the previous card.)

```html
<!DOCTYPE html>
<html lang="en">
<head>
<meta charset="utf-8">
<title>MPold Realty Business Card</title>
<link rel="stylesheet" href="https://fonts.googleapis.com/css2?family=Montserrat:wght@500;600;700&display=swap">
<style>
  :root {
    --bg: #5b5b5d;
    --card-dark: #262627;
    --card-back: #232324;
    --brand-red: #b2202e;
    --text-light: #f2f2f2;
    --emboss: #3a3a3b;
    --photo-green: #7d9a62;
    --photo-grey: #6b6f70;
  }
  * { box-sizing: border-box; margin: 0; padding: 0; }
  html, body {
    width: 1200px; height: 1021px; overflow: hidden;
    background: var(--bg);
    font-family: "Montserrat", sans-serif;
  }
  .card {
    position: absolute;
    width: 760px; height: 434px;
    box-shadow: 0 18px 40px rgba(0,0,0,.45);
    overflow: hidden;
  }
  /* Back of card */
  .card-back {
    left: 360px; top: 50px;
    background: var(--card-back);
    display: flex; align-items: center; justify-content: center;
  }
  .brand {
    display: flex; align-items: center; gap: 14px;
    font-weight: 600; letter-spacing: .22em; text-transform: uppercase;
    white-space: nowrap; line-height: 1;
  }
  .brand-mark { width: 24px; height: 24px; flex: none; }
  .card-back .brand { color: var(--emboss); font-size: 42px; letter-spacing: .26em; gap: 18px; }
  .card-back .brand-mark { background: var(--emboss); width: 34px; height: 34px; }

  /* Front of card */
  .card-front {
    left: 80px; top: 537px;
    background: var(--card-dark);
  }
  .portrait {
    position: absolute; left: 0; top: 0;
    width: 318px; height: 434px;
    background: linear-gradient(160deg, var(--photo-green) 0%, #8f9281 45%, var(--photo-grey) 100%);
  }
  .front-brand {
    position: absolute; left: 360px; top: 72px;
  }
  .front-brand .brand { color: var(--text-light); font-size: 28px; }
  .front-brand .brand-mark { background: var(--brand-red); }
  .front-brand .rule {
    height: 2px; background: var(--text-light); margin-top: 12px; width: 368px;
  }
  .agent { position: absolute; left: 360px; top: 150px; }
  .agent-name {
    color: var(--brand-red); font-weight: 700; font-size: 28px; letter-spacing: .02em; line-height: 1.15;
  }
  .agent-title {
    color: var(--text-light); font-weight: 500; font-size: 20px; margin-top: 4px;
  }
  .contact {
    position: absolute; left: 352px; top: 254px;
    list-style: none; color: var(--text-light);
    font-weight: 500; font-size: 21px;
  }
  .contact li { display: flex; align-items: center; gap: 12px; height: 31px; }
  .contact svg { width: 18px; height: 18px; flex: none; }

  .info-band {
    position: absolute; left: 318px; right: 0; bottom: 0; height: 72px;
    background: var(--brand-red);
    display: flex; align-items: center; justify-content: space-between;
    padding: 0 22px 0 30px;
  }
  .social {
    display: flex; align-items: center; gap: 12px;
    color: var(--text-light); font-weight: 500; font-size: 20px; white-space: nowrap;
  }
  .social-dot {
    width: 24px; height: 24px; border-radius: 50%;
    border: 2.5px solid var(--text-light); flex: none;
  }
  .badges { display: flex; gap: 12px; flex: none; }
  .badge {
    width: 34px; height: 34px; border: 2.5px solid var(--text-light);
    border-radius: 3px;
  }
</style>
</head>
<body>

<section class="card card-back" aria-label="Card back">
  <div class="brand"><span class="brand-mark"></span>MPold Realty</div>
</section>

<section class="card card-front" aria-label="Card front">
  <div class="portrait" role="img" aria-label="Portrait photo of the agent in a grey blazer, outdoors with greenery behind"></div>

  <div class="front-brand">
    <div class="brand"><span class="brand-mark"></span>MPold Realty</div>
    <div class="rule"></div>
  </div>

  <div class="agent">
    <p class="agent-name">Marvin Pold</p>
    <p class="agent-title">Broker/Owner</p>
  </div>

  <ul class="contact">
    <li>
      <svg viewBox="0 0 24 24" fill="#b2202e"><path d="M6.6 10.8a15 15 0 0 0 6.6 6.6l2.2-2.2a1 1 0 0 1 1-.25 11.4 11.4 0 0 0 3.6.57 1 1 0 0 1 1 1V20a1 1 0 0 1-1 1A17 17 0 0 1 3 4a1 1 0 0 1 1-1h3.5a1 1 0 0 1 1 1c0 1.25.2 2.45.57 3.57a1 1 0 0 1-.25 1z"/></svg>
      555.210.3367
    </li>
    <li>
      <svg viewBox="0 0 24 24" fill="none" stroke="#b2202e" stroke-width="2"><rect x="2" y="5" width="20" height="14" rx="1"/><path d="M2 6l10 7 10-7"/></svg>
      Marvin@MPoldRealty.com
    </li>
    <li>
      <svg viewBox="0 0 24 24" fill="none" stroke="#b2202e" stroke-width="2"><circle cx="12" cy="12" r="10"/><path d="M2 12h20M12 2a15 15 0 0 1 0 20M12 2a15 15 0 0 0 0 20"/></svg>
      www.MPoldRealty.com
    </li>
  </ul>

  <div class="info-band">
    <div class="social"><span class="social-dot"></span>the_pinecrest_realtor</div>
    <div class="badges">
      <span class="badge"></span>
      <span class="badge"></span>
    </div>
  </div>
</section>

</body>
</html>
```